Velmor Partners - website for real estate investment company

Create a bold, modern website that reflects Velmor’s success, professionalism, and credibility.
The design must stand out while maintaining a polished, corporate tone. (bold, but understated)
The client just created a new logo, and the website design must be in sync with the logo design. Information about the logo colors, fonts, and message are in the attached design brief.

Target Market(s)

b2b: banks, brokers, institutional partners, vendors, and property sellers.

Industry/Entity Type

real estate investment company

Number of Pages Required

1 page

Font styles to use
Sans Serif

Colors

Designer to choose colors to be used in the design.

Requirements
Must have
• 1. homepage design (psd) 2. a top banner image (psd) for a default inner page
Nice to have
• please see attached design brief
Should not have

```html
<!DOCTYPE html>
<html lang="en">
<head>
<meta charset="utf-8">
<title>Velmor Partners</title>
<link href="https://fonts.googleapis.com/css2?family=Poppins:wght@400;500;600;700&display=swap" rel="stylesheet">
<style>
:root{
  --red:#e31e24;
  --dark:#4a4a4a;
  --ink:#1e1e1e;
  --muted:#6b6b6b;
  --card:#f4f4f4;
  --pink:#fdeced;
  --white:#fff;
}
*{box-sizing:border-box;margin:0;padding:0}
html,body{width:1200px;height:3814px;overflow:hidden}
body{font-family:"Poppins",sans-serif;color:var(--ink);background:var(--white);position:relative}
.abs{position:absolute}
.topbar{left:0;top:0;width:1200px;height:34px;background:var(--red);color:#fff;font-size:13px;display:flex;justify-content:flex-end;align-items:center;gap:40px;padding-right:60px}
.topbar span{display:flex;align-items:center;gap:8px}
.header{left:0;top:34px;width:1200px;height:74px}
.brand{position:absolute;left:60px;top:14px;font-weight:700;font-size:40px;line-height:46px;color:var(--dark);letter-spacing:1px}
.nav-link{position:absolute;top:28px;font-size:13.5px;line-height:18px;color:var(--ink);white-space:nowrap}
.btn{display:inline-flex;align-items:center;justify-content:center;background:var(--red);color:#fff;font-weight:600;font-size:15px}
.header .btn{position:absolute;left:990px;top:16px;width:150px;height:42px}
.hero{left:0;top:108px;width:1200px;height:566px;overflow:hidden}
.hero-photo{position:absolute;inset:0;background:linear-gradient(100deg,#3f4850 0%,#5a5650 35%,#7a4a35 60%,#8b5a40 80%,#5e3d2c 100%)}
.hero-shade{position:absolute;inset:0;background:linear-gradient(90deg,rgba(20,25,35,.75) 0%,rgba(20,25,35,.3) 45%,rgba(0,0,0,0) 70%)}
.hero h1{position:absolute;left:61px;top:124px;color:#fff;font-weight:700;font-size:44px;line-height:53px}
.hero p{position:absolute;left:61px;top:240px;width:420px;color:#fff;font-size:16px;line-height:24px}
.hero .btn{position:absolute;left:59px;top:335px;width:151px;height:40px}
.stat{top:694px;width:300px;text-align:center}
.stat b{display:block;font-weight:600;font-size:38px;color:var(--ink);line-height:48px}
.stat small{display:block;font-size:12px;font-weight:600;line-height:19px;text-transform:uppercase}
.vline{width:1px;background:#d9d9d9}
.h2{width:1200px;left:0;text-align:center;font-weight:600;font-size:30px;color:var(--ink)}
.card{top:942px;width:258px;height:258px;background:var(--card);border-radius:14px;overflow:hidden}
.card.active{background:var(--pink)}
.card svg.corner{position:absolute;left:0;top:0}
.card h3{position:absolute;left:34px;top:104px;font-size:17px;font-weight:600;line-height:23px;color:#333}
.card p{position:absolute;left:34px;top:157px;width:195px;font-size:12.5px;line-height:19.5px;color:var(--muted)}
.band{left:0;width:1200px;overflow:hidden}
.band-photo{position:absolute;inset:0}
.band-shade{position:absolute;inset:0;background:rgba(20,25,35,.55)}
.band h2{position:absolute;left:0;width:1200px;text-align:center;color:#fff;font-weight:600;font-size:30px;line-height:37px}
.band p{position:absolute;left:290px;width:620px;text-align:center;color:#fff;font-size:14px;line-height:21px}
.band .btn{position:absolute;left:525px;width:150px;height:40px}
.feature{left:619px;width:448px;height:146px;background:var(--card);border-radius:14px;overflow:hidden}
.feature .num{position:absolute;left:0;top:0;width:81px;height:146px;background:var(--dark);color:#5c5c5c;font-weight:700;font-size:110px;line-height:146px;text-align:center}
.feature .ic{position:absolute;left:50px;top:43px;width:60px;height:60px;border-radius:50%;background:#fff;box-shadow:0 2px 6px rgba(0,0,0,.15);display:flex;align-items:center;justify-content:center}
.feature h3{position:absolute;left:151px;top:30px;font-size:17px;font-weight:500;color:#333}
.feature p{position:absolute;left:151px;top:64px;width:250px;font-size:12.5px;line-height:19.5px;color:var(--muted)}
.ci{left:227px;font-size:13px;color:var(--ink)}
.ci b{display:block;font-size:16px;font-weight:600;line-height:21px;margin-top:3px}
.ci svg{position:absolute;left:0;top:2px}
.ci div{margin-left:39px}
.field{border:1px solid #d8d8d8;background:#f6f6f6;color:#666;font-size:13px;padding:0 18px;display:flex;align-items:center}
.field.focus{background:var(--dark);color:#fff;border-color:var(--dark)}
.footer{left:0;top:3473px;width:1200px;height:341px;background:var(--dark);color:#fff;overflow:hidden}
.fcol{position:absolute;top:98px;font-size:13px;line-height:22.5px}
.fcol h4{font-size:17px;font-weight:500;margin-bottom:10px}
</style>
</head>
<body>

<div class="abs topbar">
  <span><svg width="16" height="16" viewBox="0 0 24 24"><path fill="#fff" d="M6.6 10.8c1.4 2.8 3.8 5.1 6.6 6.6l2.2-2.2c.3-.3.7-.4 1-.2 1.1.4 2.3.6 3.6.6.6 0 1 .4 1 1V20c0 .6-.4 1-1 1C10.6 21 3 13.4 3 4c0-.6.4-1 1-1h3.5c.6 0 1 .4 1 1 0 1.3.2 2.5.6 3.6.1.3 0 .7-.2 1z"/></svg>+ (555) 014-2208</span>
  <span><svg width="14" height="18" viewBox="0 0 24 30"><path fill="#fff" d="M12 0C5.4 0 0 5.4 0 12c0 9 12 18 12 18s12-9 12-18C24 5.4 18.6 0 12 0zm0 17a5 5 0 110-10 5 5 0 010 10z"/></svg>420 Harbor Way, Lakeview, NJ 08000</span>
</div>

<header class="abs header">
  <div class="brand">VELMOR</div>
  <nav>
    <span class="nav-link" style="left:300px">Home</span>
    <span class="nav-link" style="left:372px">Our Story</span>
    <span class="nav-link" style="left:466px">Investment Strategy</span>
    <span class="nav-link" style="left:636px">What Sets Us Apart</span>
    <span class="nav-link" style="left:799px">Our Portfolio</span>
    <span class="nav-link" style="left:912px">Contact</span>
  </nav>
  <span class="btn">Get Started</span>
</header>

<section class="abs hero">
  <div class="hero-photo" role="img" aria-label="Row of red brick terraced townhouses under a cloudy sky"></div>
  <div class="hero-shade"></div>
  <h1>EXPERIENCE.<br>STRATEGY. VISION</h1>
  <p>Velmor Partners is a vertically integrated real estate investment firm with a proven four-decade track record.</p>
  <span class="btn">Contact Us</span>
  <svg class="abs" style="left:0;bottom:0" width="1200" height="66" viewBox="0 0 1200 66"><polygon points="0,6 480,24 1200,66 0,66" fill="#e31e24"/><polygon points="0,66 480,24 1200,46 1200,66" fill="#fff"/></svg>
</section>

<div class="abs stat" style="left:130px"><b>1989</b><small>Founded</small></div>
<div class="abs vline" style="left:415px;top:684px;height:112px"></div>
<div class="abs stat" style="left:425px;top:684px"><b>23,000+</b><small>Multifamily &amp;<br>healthcare units</small></div>
<div class="abs vline" style="left:736px;top:684px;height:112px"></div>
<div class="abs stat" style="left:739px;top:684px"><b>$300M+</b><small>Invested in<br>Enovations</small></div>

<h2 class="abs h2" style="top:866px">INVESTMENT STRATEGY</h2>

<div class="abs card" style="left:59px">
  <svg class="corner" width="105" height="105" viewBox="0 0 105 105"><polygon points="0,0 105,0 0,105" fill="#4a4a4a"/><rect x="26" y="24" width="30" height="26" rx="3" fill="none" stroke="#fff" stroke-width="2"/></svg>
  <h3>Disciplined<br>Acquisition</h3>
  <p>Lorem Ipsum has been the industry's standard dummy text ever since the 1500s, when an unknown printer</p>
</div>
<div class="abs card active" style="left:333px">
  <svg class="corner" width="105" height="105" viewBox="0 0 105 105"><polygon points="0,0 105,0 0,105" fill="#e31e24"/><circle cx="51" cy="55" r="17" fill="none" stroke="#fff" stroke-width="2"/><path d="M41 56 L51 47 L61 56 M44 54 V64 H58 V54" fill="none" stroke="#fff" stroke-width="2"/></svg>
  <h3>Value-Add<br>Renovations</h3>
  <p>Lorem Ipsum has been the industry's standard dummy text ever since the 1500s, when an unknown printer</p>
</div>
<div class="abs card" style="left:607px">
  <svg class="corner" width="105" height="105" viewBox="0 0 105 105"><polygon points="0,0 105,0 0,105" fill="#4a4a4a"/><rect x="27" y="34" width="30" height="20" rx="2" fill="none" stroke="#fff" stroke-width="2"/><circle cx="60" cy="30" r="6" fill="none" stroke="#fff" stroke-width="2"/></svg>
  <h3>Long- term<br>Operations</h3>
  <p>Lorem Ipsum has been the industry's standard dummy text ever since the 1500s, when an unknown printer</p>
</div>
<div class="abs card" style="left:881px">
  <svg class="corner" width="105" height="105" viewBox="0 0 105 105"><polygon points="0,0 105,0 0,105" fill="#4a4a4a"/><path d="M30 62 V52 M38 62 V46 M46 62 V40 M54 62 V34" stroke="#fff" stroke-width="3"/><circle cx="74" cy="28" r="7" fill="none" stroke="#fff" stroke-width="2"/></svg>
  <h3>Risk-Adjusted<br>Returns</h3>
  <p>Lorem Ipsum has been the industry's standard dummy text ever since the 1500s, when an unknown printer</p>
</div>

<section class="abs band" style="top:1277px;height:488px">
  <div class="band-photo" role="img" aria-label="City skyline at dusk with skyscrapers" style="background:linear-gradient(180deg,#5b6470 0%,#3a4350 50%,#2a2f38 100%)"></div>
  <div class="band-shade"></div>
  <svg class="abs" style="left:0;top:0" width="1200" height="488" viewBox="0 0 1200 488"><polygon points="0,0 1200,0 1200,58 700,40" fill="#fff"/><polygon points="700,40 1200,0 1200,58" fill="#e31e24"/><polygon points="0,430 520,488 0,488" fill="#e31e24"/><polygon points="0,488 520,488 1200,450 1200,488" fill="#fff"/></svg>
  <h2 style="top:104px">OUR STORY</h2>
  <p style="top:155px">Lorem Ipsum has been the industry’s standard dummy text ever since the 1500s, when an unknown printer took a galley of type and scrambled it to make a type specimen book. It has survived not only five centuries, but also the leap into electronic typesetting, remaining essentially unchanged.</p>
  <p style="top:252px">Lorem Ipsum has been the industry’s standard dummy text ever since the 1500s, when an unknown printer took a galley of type and scrambled it to make a type specimen book. It has survived not only five centuries, but also the leap into electronic</p>
  <span class="btn" style="top:340px">View Stoury</span>
</section>

<h2 class="abs h2" style="top:1836px">WHAT SEATS US APART</h2>

<div class="abs" style="left:173px;top:2110px;width:360px;text-align:center;font-weight:700;font-size:72px;color:var(--dark);letter-spacing:2px">VELMOR</div>

<div class="abs feature" style="top:1916px">
  <div class="num">1</div>
  <div class="ic"><svg width="30" height="30" viewBox="0 0 30 30"><circle cx="13" cy="13" r="9" fill="none" stroke="#e31e24" stroke-width="2"/><path d="M20 20 L27 27" stroke="#4a4a4a" stroke-width="3"/></svg></div>
  <h3>Discover properties</h3>
  <p>Lorem Ipsum has been the industry's standard dummy text ever since the 1500s</p>
</div>
<div class="abs feature" style="top:2077px">
  <div class="num">2</div>
  <div class="ic"><svg width="30" height="30" viewBox="0 0 30 30"><path d="M6 27 V20 M12 27 V15 M18 27 V10 M24 27 V5" stroke="#e31e24" stroke-width="3"/><path d="M4 16 L14 7 L18 10 L26 3" fill="none" stroke="#4a4a4a" stroke-width="2"/></svg></div>
  <h3>Invest With Confidence</h3>
  <p>Lorem Ipsum has been the industry's standard dummy text ever since the 1500s</p>
</div>
<div class="abs feature" style="top:2239px">
  <div class="num">3</div>
  <div class="ic"><svg width="30" height="30" viewBox="0 0 30 30"><rect x="12" y="4" width="14" height="12" rx="2" fill="none" stroke="#4a4a4a" stroke-width="2"/><path d="M3 22 Q10 18 16 22 L26 19" fill="none" stroke="#e31e24" stroke-width="2"/></svg></div>
  <h3>Earn &amp; track</h3>
  <p>Lorem Ipsum has been the industry's standard dummy text ever since the 1500s</p>
</div>

<section class="abs band" style="top:2459px;height:521px">
  <div class="band-photo" role="img" aria-label="Twin tower skyline with high-rise buildings at sunset" style="background:linear-gradient(180deg,#4f5a66 0%,#3c4652 55%,#2c3a32 100%)"></div>
  <div class="band-shade"></div>
  <svg class="abs" style="left:0;top:0" width="1200" height="521" viewBox="0 0 1200 521"><polygon points="0,0 1200,0 1200,2 700,42" fill="#fff"/><polygon points="700,42 1200,2 1200,60" fill="#e31e24"/><polygon points="0,460 480,480 1200,470 0,521" fill="#e31e24"/><polygon points="0,521 1200,470 1200,521" fill="#fff"/></svg>
  <h2 style="top:116px">OUR REAL- ESTATE Portfolio AT<br>YOUR FINGERTIPS</h2>
  <p style="top:200px">Lorem Ipsum has been the industry’s standard dummy text ever since the 1500s, when an unknown printer took a galley of type and scrambled it to make a type specimen book. It has survived not only five centuries, but also the leap into electronic typesetting, remaining essentially unchanged.</p>
  <p style="top:292px">Lorem Ipsum has been the industry’s standard dummy text ever since the 1500s, when an unknown printer took a galley of type and scrambled it to make a type specimen book. It has survived not only five centuries</p>
  <span class="btn" style="top:373px">View Stoury</span>
</section>

<h2 class="abs h2" style="top:3050px">CONTACT US</h2>

<div class="abs ci" style="top:3138px">
  <svg width="20" height="20" viewBox="0 0 24 24"><path fill="#e31e24" d="M6.6 10.8c1.4 2.8 3.8 5.1 6.6 6.6l2.2-2.2c.3-.3.7-.4 1-.2 1.1.4 2.3.6 3.6.6.6 0 1 .4 1 1V20c0 .6-.4 1-1 1C10.6 21 3 13.4 3 4c0-.6.4-1 1-1h3.5c.6 0 1 .4 1 1 0 1.3.2 2.5.6 3.6.1.3 0 .7-.2 1z"/></svg>
  <div>Call Now<b>+ (555) 014-2208</b></div>
</div>
<div class="abs ci" style="top:3202px">
  <svg width="20" height="16" viewBox="0 0 24 18"><rect width="24" height="18" rx="2" fill="#e31e24"/><path d="M1 2 L12 10 L23 2" fill="none" stroke="#fff" stroke-width="2"/></svg>
  <div>Email<b>info@velmor.com</b></div>
</div>
<div class="abs ci" style="top:3264px">
  <svg width="16" height="20" viewBox="0 0 24 30"><path fill="#e31e24" d="M12 0C5.4 0 0 5.4 0 12c0 9 12 18 12 18s12-9 12-18C24 5.4 18.6 0 12 0zm0 17a5 5 0 110-10 5 5 0 010 10z"/></svg>
  <div>Location<b>420 Harbor Way, Lakeview,<br>NJ 08000</b></div>
</div>
<div class="abs vline" style="left:489px;top:3118px;height:276px"></div>

<div class="abs field focus" style="left:545px;top:3131px;width:218px;height:42px">First name *</div>
<div class="abs field" style="left:775px;top:3131px;width:219px;height:42px">Last name *</div>
<div class="abs field" style="left:545px;top:3183px;width:218px;height:42px">Email *</div>
<div class="abs field" style="left:775px;top:3183px;width:219px;height:42px">Phone no *</div>
<div class="abs field" style="left:545px;top:3239px;width:449px;height:91px;align-items:flex-start;padding-top:18px">Message *</div>
<span class="abs btn" style="left:547px;top:3341px;width:134px;height:42px">SUBMIT</span>

<footer class="abs footer">
  <svg class="abs" style="left:0;top:0" width="1200" height="60" viewBox="0 0 1200 60"><polygon points="0,0 1200,0 1200,0 760,38" fill="#fff"/><polygon points="760,38 1200,0 1200,58" fill="#e31e24"/></svg>
  <div class="abs" style="left:59px;top:92px;font-weight:700;font-size:40px;letter-spacing:1px">VELMOR</div>
  <div class="fcol" style="left:335px"><h4>Company</h4>Home<br>Our Story<br>Investment Strategy<br>What Sets Us Apart<br>Our Portfolio<br>Contact</div>
  <div class="fcol" style="left:609px"><h4>Investment Strategy</h4>Disciplined Acquisitions<br>Value-Add Renovations<br>Long-Term Operations<br>Risk-Adjusted Returns</div>
  <div class="fcol" style="left:883px;width:200px"><h4>Contact Us</h4>
    <div style="position:relative;padding-left:35px;margin-top:6px">
      <svg style="position:absolute;left:0;top:4px" width="18" height="18" viewBox="0 0 24 24"><path fill="#e31e24" d="M6.6 10.8c1.4 2.8 3.8 5.1 6.6 6.6l2.2-2.2c.3-.3.7-.4 1-.2 1.1.4 2.3.6 3.6.6.6 0 1 .4 1 1V20c0 .6-.4 1-1 1C10.6 21 3 13.4 3 4c0-.6.4-1 1-1h3.5c.6 0 1 .4 1 1 0 1.3.2 2.5.6 3.6.1.3 0 .7-.2 1z"/></svg>
      Call Now<br><b style="font-size:15px;font-weight:600">+ (555) 014-2208</b>
    </div>
    <div style="position:relative;padding-left:35px;margin-top:22px">
      <svg style="position:absolute;left:0;top:4px" width="15" height="19" viewBox="0 0 24 30"><path fill="#e31e24" d="M12 0C5.4 0 0 5.4 0 12c0 9 12 18 12 18s12-9 12-18C24 5.4 18.6 0 12 0zm0 17a5 5 0 110-10 5 5 0 010 10z"/></svg>
      Location<br><b style="font-size:15px;font-weight:600">420 Harbor Way, Lakeview, NJ 08000</b>
    </div>
  </div>
  <div class="abs" style="left:59px;top:284px;width:1080px;height:1px;background:#6a6a6a"></div>
  <div class="abs" style="left:0;top:297px;width:1200px;text-align:center;font-size:12.5px">Copyright ©2025 velmor.All rights reserved</div>
</footer>

</body>
</html>
```